Corrigan Architecture (business card)

We need a business card design. We are a full service architectural firm that specializes in mostly residential projects and some commercial projects. We are located in Hudson Valley, New York. We work with high end clients and want a business card that is memorable and has a sleek, modern, design but will not go out of style (timeless).

Target Market(s)

high end residential clients

Industry/Entity Type

Architect

Contact Information for Business Card

Front of card
Company Logo
website: www.corriganarchitectur.example
what we do: residential, Commercial

back of card
Owner's Name: Dorian Corrigan
owner's title: Principal
Business address: 2873 Route 92 Suite A, Brellfordton, NY 12688
phone number: 845-608-2917
e-mail: dc@corriganarchitecture.example

We like:
icons
sleek and clean design
simple not too busy or too much text

Font styles to use
Sans Serif

Colors
0356a4

Requirements
Must have
• company colors are navy blue, white, and gray
• Front of card
• Company Logo
• website: www.corriganarchitectur.example
• what we do: residential, Commercial
• back of card
• Owner's Name: Dorian Corrigan
• owner's title: Principal
• Business address: 2873 Route 92 Suite A, Brellfordton, NY 12688
• phone number: 845-608-2917
• e-mail: dc@corriganarchitecture.example
Nice to have
• We like:
• icons
• sleek and clean design
• simple not too much text
• color of the card to be either blue or gray
Should not have
• we do not like houses in the design or plans of houses-this is over done and we don't like it.
• no QR CODES

```html
<!DOCTYPE html>
<html lang="en">
<head>
<meta charset="utf-8">
<title>Corrigan Architecture – Business Card</title>
<link rel="stylesheet" href="https://fonts.googleapis.com/css2?family=Arimo:wght@400;700&family=Questrial&display=swap">
<style>
  :root{
    --stage:#2a2a2c;
    --card:#1d1e21;
    --card-edge:#26272b;
    --navy:#2b2f8f;
    --gray-light:#c9c9cc;
    --gray-mid:#9a9a9e;
    --gray-dim:#5c5d61;
    --rule:#6a6b6f;
    --pattern-top:#232428;
    --pattern-bottom:#1d1e21;
  }
  *{box-sizing:border-box;margin:0;padding:0}
  html,body{width:1200px;height:1108px;overflow:hidden;background:var(--stage)}
  .stage{position:relative;width:1200px;height:1108px;display:flex;justify-content:center;align-items:center;gap:70px}
  .card{position:relative;width:360px;height:630px;background:var(--card);border-radius:22px;border:1px solid var(--card-edge);overflow:hidden}

  /* contact side */
  .brand{position:absolute;top:86px;left:40px;display:flex;align-items:center;gap:12px}
  .brand-mark{width:26px;height:26px;background:var(--navy)}
  .brand-name{font-family:"Questrial",sans-serif;font-size:27px;line-height:1.05;color:var(--navy);text-transform:uppercase;letter-spacing:.5px}
  .contact{position:absolute;left:0;right:0;top:330px;text-align:center;font-family:"Arimo",sans-serif;color:var(--gray-light)}
  .person-name{font-weight:700;font-size:21px;letter-spacing:.5px;text-transform:uppercase}
  .person-title{font-size:16px;color:var(--gray-mid);margin-top:2px}
  .icon-rule{display:flex;align-items:center;justify-content:center;gap:8px;margin:10px 30px 8px}
  .icon-rule::before,.icon-rule::after{content:"";flex:1;height:1px;background:var(--rule)}
  .icons{display:flex;gap:5px}
  .icons svg{width:24px;height:24px;display:block}
  .contact-line{font-size:17px;line-height:1.4}
  .divider{height:1px;background:var(--rule);margin:10px 60px 14px}
  .address{font-size:17px;line-height:1.4}

  /* brand side */
  .pattern{position:absolute;top:0;left:0;right:0;height:430px;background:linear-gradient(180deg,var(--pattern-top),var(--pattern-bottom))}
  .front-name{position:absolute;left:40px;top:440px;font-family:"Questrial",sans-serif;font-size:36px;line-height:1.02;color:var(--gray-mid);text-transform:uppercase}
  .front-site{position:absolute;left:40px;top:527px;font-family:"Questrial",sans-serif;font-size:16px;color:var(--gray-light);letter-spacing:.6px}
  .services{position:absolute;left:40px;top:568px;font-family:"Arimo",sans-serif;font-weight:700;font-size:17px;color:var(--gray-mid);letter-spacing:.6px;text-transform:uppercase}
  .services .sep{font-weight:400;margin:0 8px}
</style>
</head>
<body>
<main class="stage">
  <section class="card card-contact">
    <div class="brand">
      <span class="brand-mark"></span>
      <span class="brand-name">Corrigan<br>Architecture</span>
    </div>
    <div class="contact">
      <p class="person-name">Dorian Corrigan</p>
      <p class="person-title">Principal</p>
      <div class="icon-rule">
        <div class="icons">
          <svg viewBox="0 0 24 24" aria-label="Phone"><rect width="24" height="24" rx="3" fill="#e6e6e8"/><path d="M7 6h3l1 3-2 1.5a8 8 0 0 0 4.5 4.5L15 13l3 1v3a1 1 0 0 1-1 1A11 11 0 0 1 6 7a1 1 0 0 1 1-1z" fill="#1d1e21"/></svg>
          <svg viewBox="0 0 24 24" aria-label="Email"><rect width="24" height="24" rx="3" fill="#e6e6e8"/><rect x="5" y="7" width="14" height="10" fill="none" stroke="#1d1e21" stroke-width="1.6"/><path d="M5 7l7 6 7-6" fill="none" stroke="#1d1e21" stroke-width="1.6"/></svg>
          <svg viewBox="0 0 24 24" aria-label="Website"><rect width="24" height="24" rx="3" fill="#e6e6e8"/><circle cx="12" cy="12" r="6" fill="none" stroke="#1d1e21" stroke-width="1.6"/><path d="M6 12h12M12 6c-2.5 3-2.5 9 0 12M12 6c2.5 3 2.5 9 0 12" fill="none" stroke="#1d1e21" stroke-width="1.3"/></svg>
        </div>
      </div>
      <p class="contact-line">845-608-2917</p>
      <p class="contact-line">dc@corriganarchitecture.example</p>
      <p class="contact-line">www.corriganarchitectur.example</p>
      <div class="divider"></div>
      <p class="address">2873 Route 92 Suite A<br>Brellfordton, NY 12688</p>
    </div>
  </section>

  <section class="card card-brand">
    <div class="pattern" role="img" aria-label="Faint repeating brand pattern"></div>
    <p class="front-name">Corrigan<br>Architecture</p>
    <p class="front-site">www.corriganarchitectur.example</p>
    <p class="services">Residential<span class="sep">|</span>Commercial</p>
  </section>
</main>
</body>
</html>
```